Plastic Business Cards

I am looking for a plastic business card that matches the theme of my company.

Attached will be logo and template to Cardloom for printing.

On card please include the following information:

Logo
612-437-8916 Call or Text
www.BrightpaneMN.com

Window Cleaning
Gutter Cleaning & Covers
Christmas Lighting

200+ 5 Star Reviews

```html
<!DOCTYPE html>
<html lang="en">
<head>
<meta charset="utf-8">
<title>Brightpane Window Cleaning – Business Card</title>
<link href="https://fonts.googleapis.com/css2?family=Montserrat:wght@500;700&display=swap" rel="stylesheet">
<style>
  :root {
    --page-bg: #d8d4cd;
    --card-bg: #eef1f4;
    --card-edge: #ffffff;
    --ink: #141a22;
    --navy: #123563;
    --navy-deep: #0c2748;
    --green: #7fb02c;
    --sliver: #c9ccd1;
  }
  * { box-sizing: border-box; margin: 0; padding: 0; }
  html, body {
    width: 1200px; height: 969px; overflow: hidden;
    background: var(--page-bg);
    font-family: "Montserrat", Arial, sans-serif;
  }
  .card {
    position: absolute; left: 80px; top: 187px;
    width: 1040px; height: 594px;
    background: var(--card-bg);
    border: 1px solid var(--card-edge);
    border-radius: 26px;
    overflow: hidden;
    box-shadow: 0 10px 30px rgba(0,0,0,0.12);
  }
  .brand {
    position: absolute; left: 89px; top: 155px;
    width: 411px; height: 253px;
    display: flex; flex-direction: column; align-items: center; justify-content: center;
    gap: 18px;
  }
  .brand-dot {
    width: 92px; height: 92px; border-radius: 50%;
    background: var(--navy);
  }
  .brand-name {
    font-weight: 700; font-size: 30px; line-height: 1.2;
    color: var(--navy); text-align: center;
  }
  .divider {
    position: absolute; left: 555px; top: 194px;
    width: 2px; height: 198px; background: var(--navy);
  }
  .details {
    position: absolute; left: 597px; top: 190px;
    list-style: none; color: var(--ink);
    font-weight: 500; font-size: 23px;
  }
  .details li { display: flex; align-items: center; height: 41px; }
  .details .contact { gap: 11px; }
  .details .services-start { margin-top: 12px; }
  .icon { width: 24px; height: 24px; flex: none; }
  .bands { position: absolute; left: 0; bottom: 0; width: 1040px; height: 64px; }
</style>
</head>
<body>
  <div class="card">
    <div class="brand">
      <div class="brand-dot"></div>
      <div class="brand-name">Brightpane<br>Window Cleaning</div>
    </div>

    <div class="divider"></div>

    <ul class="details">
      <li class="contact">
        <svg class="icon" viewBox="0 0 24 24" aria-hidden="true">
          <path fill="#123563" d="M2 8c0-2 4-4 10-4s10 2 10 4v2h-5V8c-2-.7-8-.7-10 0v2H2z"/>
          <path fill="#123563" d="M6 11h12l2 9H4z"/>
          <circle cx="12" cy="15.5" r="2.2" fill="#eef1f4"/>
        </svg>
        612-437-8916 Call or Text
      </li>
      <li class="contact">
        <svg class="icon" viewBox="0 0 24 24" aria-hidden="true">
          <circle cx="12" cy="12" r="10.5" fill="#123563"/>
          <path fill="#eef1f4" d="M7 6c2 0 3 1 3 2.5S8 10 8 12s2 2 2 4-1 3-2 3c-1-1-1.5-3-2.5-4S3 13 3 11c1-3 2-5 4-5zm8 1c1.5 0 3 1 3.5 2.5-1 .5-2 0-3 1s0 2-1 2.5-2-1-2-2.5 1-3.5 2.5-3.5z"/>
        </svg>
        www.BrightpaneMN.com
      </li>
      <li class="services-start">Window Cleaning</li>
      <li>Gutter Cleaning &amp; Covers</li>
      <li>Christmas Lighting</li>
    </ul>

    <svg class="bands" viewBox="0 0 1040 64" preserveAspectRatio="none" aria-hidden="true">
      <polygon points="0,35 569,35 554,64 0,64" fill="var(--green)"/>
      <polygon points="569,35 576,35 561,64 554,64" fill="var(--sliver)"/>
      <polygon points="605,0 1040,0 1040,64 546,64" fill="var(--navy-deep)"/>
    </svg>
  </div>
</body>
</html>
```